Civil Engineering Web design

.Net Web design for a civil engineering company to include a blog page, I will like a site similar to this http://www.layoutgrove.example/demo/58273.html

company name: Dorvil Associates

-Civil/Structural Engineering Solutions

-Engineering Design Development and Consultancy

More Information about the internal pages or links:
1. Each one of the menu choices will take you to a page for that option where I will be able to insert text 2. Our team likewise should be a page with space for a photo of the staff and text space for inserting employee name and title, qualifications and job description and work experience...
Can we have 3 groups for these
Management Staff
Support Staff
Other Staff

3. The blog is a generic blog page where users can add comments to a any subjects raised by our team and submit... When they submit, the comments should be emailed to us 4. Contact us is also a tool for emailing us by users, whereby they provide their email, subject and email body 5. projects is a page that allows insertion of title, one photo and description of the project...
6. services is a page with links on the left for Construction Supervision Civil and Structured Engineering Designs Corporate Recognition

Each on when clicked should display the relevant information for the link which is a gallery of two photos side by side and one description per pair...

Industry/Entity Type

Construction

Requirements
Must have
• User ability to manage content; not design

Pages:
Home
Services
Projects (sub page picture gallery)
Reference
Our Team
Blog
Contact Us

```html
<!DOCTYPE html>
<html lang="en">
<head>
<meta charset="utf-8">
<title>Civil Services</title>
<link rel="stylesheet" href="https://fonts.googleapis.com/css2?family=Raleway:wght@700;800&family=Ubuntu:wght@300;400&family=Lato:wght@300;400&display=swap">
<style>
  :root {
    --sky-light: #e9eef7;
    --sky-mid: #b9c8e3;
    --helmet-yellow: #f3c315;
    --helmet-deep: #e0a400;
    --logo-grey: #5a5a5a;
    --sidebar-bg: #f1f1f1;
    --nav-bg: #e6e6e6;
    --nav-border: #c9c9c9;
    --nav-text: #1c1c1c;
    --accent: #00c8f8;
    --panel: rgba(28, 28, 30, 0.9);
    --panel-solid: #1e1e20;
    --text-light: #ffffff;
    --text-muted: #b9b9b9;
    --rule: #6a6a6a;
  }
  * { box-sizing: border-box; margin: 0; padding: 0; }
  html, body { width: 1200px; height: 773px; overflow: hidden; }
  body {
    position: relative;
    font-family: "Lato", sans-serif;
    background: var(--sky-light);
  }
  .backdrop {
    position: absolute; inset: 0;
    background:
      radial-gradient(ellipse 420px 360px at 1010px 180px, var(--helmet-yellow) 0%, var(--helmet-deep) 45%, rgba(224,164,0,0) 75%),
      linear-gradient(120deg, var(--sky-mid) 0%, var(--sky-light) 35%, #dfe6f2 60%, var(--sky-mid) 100%);
  }
  .sidebar {
    position: absolute; left: 109px; top: 0; width: 200px; height: 773px;
    background: var(--sidebar-bg);
  }
  .logo-box {
    height: 127px; background: var(--logo-grey);
    display: flex; align-items: center; justify-content: center; text-align: center;
    color: var(--text-light); font-family: "Raleway", sans-serif; font-weight: 700;
    font-size: 26px; line-height: 31px;
  }
  .main-nav { list-style: none; position: absolute; top: 225px; left: 0; width: 200px; }
  .main-nav li {
    height: 39px; margin-bottom: 30px;
    background: var(--nav-bg); border: 1px solid var(--nav-border);
    display: flex; align-items: center; padding-left: 23px;
    font-family: "Raleway", sans-serif; font-weight: 700; font-size: 17px; color: var(--nav-text);
  }
  .social-bar {
    position: absolute; left: 0; bottom: 0; width: 200px; height: 39px;
    background: var(--accent);
    display: flex; justify-content: space-around; align-items: center;
  }
  .social-dot { width: 9px; height: 9px; border-radius: 50%; background: var(--text-light); }
  .site-title {
    position: absolute; left: 364px; top: 28px;
    font-family: "Raleway", sans-serif; font-weight: 800; font-size: 41px; color: #111;
    letter-spacing: 0.5px;
  }
  .call-bar {
    position: absolute; left: 801px; top: 76px; width: 292px; height: 44px;
  }
  .call-bar svg { position: absolute; inset: 0; }
  .call-bar span {
    position: absolute; left: 50px; top: 13px;
    color: var(--text-light); font-size: 16.5px;
  }
  .content-panel {
    position: absolute; left: 365px; top: 120px; width: 728px; height: 653px;
    background: var(--panel); padding: 0 40px;
  }
  .panel-heading {
    font-family: "Ubuntu", sans-serif; font-weight: 400; font-size: 26px;
    color: var(--text-light); margin-top: 19px; line-height: 30px;
  }
  .banner {
    margin-top: 17px; width: 644px; height: 128px;
    background: radial-gradient(ellipse 260px 90px at 320px 40px, #fbe33a 0%, #f5b516 50%, #ea7a1e 100%);
  }
  .tagline { margin-top: 19px; font-size: 16.5px; color: var(--text-light); }
  .intro {
    margin-top: 12px; font-size: 13px; line-height: 20.5px; color: var(--text-muted); width: 620px;
  }
  .read-more {
    display: inline-block; margin-top: 20px; height: 31px; width: 90px;
    background: var(--accent); color: var(--text-light); border-radius: 5px;
    font-size: 12.5px; text-align: center; line-height: 31px;
  }
  .divider { border: 0; border-top: 1px solid var(--rule); margin-top: 30px; }
  .section-heading {
    font-family: "Ubuntu", sans-serif; font-weight: 400; font-size: 26px;
    color: var(--text-light); margin-top: 22px;
  }
  .service-grid {
    list-style: none; position: relative; margin-top: 24px; height: 180px;
  }
  .service-grid li {
    position: absolute; display: flex; align-items: center;
    font-size: 15.5px; color: #cfcfcf; text-transform: uppercase; white-space: nowrap;
  }
  .bullet {
    width: 27px; height: 27px; border-radius: 50%;
    background: var(--accent); border: 3px solid var(--text-light);
    box-shadow: inset 0 0 0 2px var(--panel-solid);
    margin-right: 11px; flex: none;
  }
</style>
</head>
<body>
  <div class="backdrop" role="img" aria-label="Architectural blueprints with a yellow hard hat, tape measure and tools"></div>

  <aside class="sidebar">
    <div class="logo-box">Company<br>Logo</div>
    <ul class="main-nav">
      <li>Home</li>
      <li>Services</li>
      <li>Projects</li>
      <li>Reference</li>
      <li>Our Team</li>
      <li>Blog</li>
      <li>Contact Us</li>
    </ul>
    <div class="social-bar" aria-label="Social links">
      <span class="social-dot"></span><span class="social-dot"></span><span class="social-dot"></span>
    </div>
  </aside>

  <h1 class="site-title">COMPANY NAME</h1>

  <div class="call-bar">
    <svg width="292" height="44" viewBox="0 0 292 44">
      <polygon points="22,0 292,0 292,44 0,44" fill="#1e1e20"/>
      <polygon points="22,0 30,0 8,44 0,44" fill="#00c8f8"/>
    </svg>
    <span>Call no: +11&nbsp; 4827360519</span>
  </div>

  <main class="content-panel">
    <h2 class="panel-heading">Welcome to civil services</h2>
    <div class="banner" role="img" aria-label="Silhouettes of cranes and construction sites on a map of the world against an orange sunset"></div>
    <p class="tagline">Raise efficiency , cut downtime , and keep your projects on time</p>
    <p class="intro">Building construction is the process of preparing for and forming buildings and building systems. Construction starts with planning, design, and financing and continues until the structure is ready for occupancy.</p>
    <a class="read-more">Read more</a>
    <hr class="divider">
    <h2 class="section-heading">Service overview</h2>
    <ul class="service-grid">
      <li style="left:0;top:0"><span class="bullet"></span>Analysis</li>
      <li style="left:0;top:43px"><span class="bullet"></span>Data&nbsp; Acquisition</li>
      <li style="left:0;top:86px"><span class="bullet"></span>Design</li>
      <li style="left:0;top:129px"><span class="bullet"></span>Electronics</li>
      <li style="left:215px;top:0"><span class="bullet"></span>Field Services</li>
      <li style="left:215px;top:43px"><span class="bullet"></span>Fitness for Service</li>
      <li style="left:215px;top:86px"><span class="bullet"></span>Floating System</li>
      <li style="left:215px;top:129px"><span class="bullet"></span>Forensic Engineering</li>
      <li style="left:462px;top:0"><span class="bullet"></span>Material / Metal</li>
      <li style="left:462px;top:43px"><span class="bullet"></span>Inst &amp; Control</li>
      <li style="left:462px;top:86px"><span class="bullet"></span>Process Tech</li>
      <li style="left:462px;top:129px"><span class="bullet"></span>Testing</li>
    </ul>
  </main>
</body>
</html>
```